new roofing company card

New primary business card for roofing company.

Industry/Entity Type

Residential roofing/Specializing in Asphalt and Standing seam metal roofing

Contact Information for Business Card

Phone number is: 555 471 2086 Email: support@halvenshingleworks.example website: www.halvenshingleworks.example

Colors
EB3D1F
EC4F4E
F09395
F8D3D4
FCEDEE

```html
<!DOCTYPE html>
<html lang="en">
<head>
<meta charset="utf-8">
<title>Halven Shingleworks – Business Card</title>
<link rel="stylesheet" href="https://fonts.googleapis.com/css2?family=Cinzel:wght@400&family=Arimo:wght@400;700&display=swap">
<style>
  :root {
    --backdrop: #3d3d3d;
    --card-dark: #2d2d2d;
    --card-light: #ffffff;
    --brand-red: #d0281c;
    --edge-red: #c9261b;
    --ink-white: #ffffff;
    --ink-dark: #2a2a2a;
    --ink-muted: #e6e6e6;
  }
  * { box-sizing: border-box; margin: 0; padding: 0; }
  html, body { width: 1200px; height: 803px; overflow: hidden; }
  body {
    background: var(--backdrop);
    display: flex;
    align-items: center;
    justify-content: center;
    gap: 48px;
    font-family: "Arimo", Arial, sans-serif;
  }
  .card {
    position: relative;
    width: 525px;
    height: 300px;
    border-radius: 18px;
    box-shadow: 0 4px 0 var(--edge-red), 0 18px 30px rgba(0,0,0,0.35);
    overflow: hidden;
  }
  .card--front { background: var(--card-dark); }
  .card--back {
    background: var(--card-light);
    display: flex;
    align-items: center;
    justify-content: center;
  }

  .front-brand {
    position: absolute;
    left: 38px;
    top: 112px;
    font-family: "Cinzel", Georgia, serif;
    font-weight: 400;
    font-size: 26px;
    letter-spacing: 1px;
    color: var(--ink-white);
    line-height: 1;
  }
  .front-rule {
    position: absolute;
    left: 38px;
    top: 150px;
    width: 250px;
    height: 2px;
    background: var(--brand-red);
  }
  .person {
    position: absolute;
    left: 38px;
    top: 168px;
  }
  .person__name {
    font-weight: 700;
    font-size: 17px;
    letter-spacing: 0.5px;
    color: var(--brand-red);
  }
  .person__role {
    margin-top: 3px;
    font-size: 12px;
    color: var(--ink-muted);
  }
  .contacts {
    position: absolute;
    left: 38px;
    top: 222px;
    list-style: none;
  }
  .contacts__item {
    display: flex;
    align-items: center;
    gap: 8px;
    font-size: 12.5px;
    color: var(--ink-white);
    line-height: 19px;
  }
  .contacts__icon { width: 11px; height: 11px; fill: var(--brand-red); flex: none; }

  .back-brand {
    display: flex;
    align-items: center;
    gap: 12px;
  }
  .back-brand__mark {
    width: 18px;
    height: 18px;
    background: var(--brand-red);
  }
  .back-brand__name {
    font-family: "Cinzel", Georgia, serif;
    font-weight: 400;
    font-size: 30px;
    color: var(--ink-dark);
    letter-spacing: 1px;
  }
</style>
</head>
<body>
  <section class="card card--front" aria-label="Card front">
    <p class="front-brand">Halven Shingleworks</p>
    <div class="front-rule"></div>
    <div class="person">
      <p class="person__name">DANA MERCER</p>
      <p class="person__role">President</p>
    </div>
    <ul class="contacts">
      <li class="contacts__item">
        <svg class="contacts__icon" viewBox="0 0 24 24" aria-hidden="true"><path d="M6.6 10.8a15.1 15.1 0 0 0 6.6 6.6l2.2-2.2a1 1 0 0 1 1-.25 11.4 11.4 0 0 0 3.6.57 1 1 0 0 1 1 1V20a1 1 0 0 1-1 1A17 17 0 0 1 3 4a1 1 0 0 1 1-1h3.5a1 1 0 0 1 1 1c0 1.25.2 2.45.57 3.57a1 1 0 0 1-.25 1z"/></svg>
        555 471 2086
      </li>
      <li class="contacts__item">
        <svg class="contacts__icon" viewBox="0 0 24 24" aria-hidden="true"><path d="M2 5h20v14H2z M4 7v.4l8 5 8-5V7l-8 5z" fill-rule="evenodd"/></svg>
        support@halvenshingleworks.example
      </li>
      <li class="contacts__item">
        <svg class="contacts__icon" viewBox="0 0 24 24" aria-hidden="true"><circle cx="12" cy="12" r="10"/></svg>
        www.halvenshingleworks.example
      </li>
    </ul>
  </section>

  <section class="card card--back" aria-label="Card back">
    <div class="back-brand">
      <span class="back-brand__mark" aria-hidden="true"></span>
      <span class="back-brand__name">Halven Shingleworks</span>
    </div>
  </section>
</body>
</html>
```